Powerpoint template & style design project

KLavender Consulting is an IT technology firm specializing in mobility and telecommunications applications. We provide technical consulting to global companies that want to build mobile applications and take critical business applications and move them into the cloud.
We would like to see designs that use the color blue. The final design should communicate confidence, agility and speak to technology focused customers. Forward progress and/or motion should be conveyed.

Target Market(s)

Government customers and large enterprise companies

Industry/Entity Type

Telecommunications

Font styles to use
Sans Serif

Colors
0555a3

Requirements
Must have
• different slides: Cover page, title slide, main content, transition slide, close out slide..

```html
<!DOCTYPE html>
<html lang="en">
<head>
<meta charset="utf-8">
<title>KLavender Consulting – Presentation Template</title>
<link href="https://fonts.googleapis.com/css2?family=Arimo:wght@700&family=Nunito:wght@800&display=swap" rel="stylesheet">
<style>
  :root {
    --board: #666666;
    --paper: #ffffff;
    --navy: #021a3f;
    --ink: #000000;
    --media-light: #4f9fe6;
    --media-mid: #0b4c9a;
    --media-dark: #03142f;
  }
  * { margin: 0; padding: 0; box-sizing: border-box; }
  html, body { width: 1200px; height: 1000px; overflow: hidden; background: var(--board); }
  .sheet { position: relative; width: 1200px; height: 1000px; }
  .slide {
    position: absolute; width: 549px; height: 455px;
    background: var(--paper); overflow: hidden;
  }
  .slide--cover   { left: 20px;  top: 20px; }
  .slide--content { left: 631px; top: 20px; }
  .slide--media   { left: 20px;  top: 524px; background: var(--navy); }
  .slide--closing { left: 631px; top: 524px; }
  .wave { position: absolute; left: 0; bottom: 0; width: 549px; height: 455px; }
  .cover-title {
    position: absolute; left: 0; width: 549px; top: 166px;
    text-align: center; font-family: "Arimo", Arial, sans-serif; font-weight: 700;
    font-size: 31px; line-height: 39px; color: var(--ink);
  }
  .brand-name {
    position: absolute; font-family: "Nunito", sans-serif; font-weight: 800;
    color: var(--navy); white-space: nowrap; letter-spacing: -0.5px;
  }
  .brand-name--corner { right: 18px; top: 358px; font-size: 17px; }
  .brand-name--light { color: var(--paper); top: 408px; }
  .brand-name--hero { left: 0; width: 549px; text-align: center; top: 232px; font-size: 40px; letter-spacing: -1px; }
  .media-panel {
    position: absolute; left: 59px; top: 49px; width: 434px; height: 287px;
    background: radial-gradient(ellipse at 45% 45%, var(--media-light) 0%, var(--media-mid) 40%, var(--media-dark) 100%);
  }
</style>
</head>
<body>
<div class="sheet">

  <section class="slide slide--cover">
    <h1 class="cover-title">KLavender Consulting<br>Welcome to presentation<br>April 2015</h1>
    <p class="brand-name brand-name--corner">KLavender Consulting</p>
    <svg class="wave" viewBox="0 0 549 455" aria-hidden="true">
      <path d="M0,370 C150,398 360,402 549,412 L549,455 L0,455 Z" fill="var(--navy)"/>
      <path d="M0,395 C160,418 360,398 549,424" fill="none" stroke="var(--paper)" stroke-width="5"/>
      <path d="M0,417 C190,440 390,418 549,437" fill="none" stroke="var(--paper)" stroke-width="4"/>
    </svg>
  </section>

  <section class="slide slide--content">
    <p class="brand-name brand-name--corner">KLavender Consulting</p>
    <svg class="wave" viewBox="0 0 549 455" aria-hidden="true">
      <path d="M0,370 C150,398 360,402 549,412 L549,455 L0,455 Z" fill="var(--navy)"/>
      <path d="M0,395 C160,418 360,398 549,424" fill="none" stroke="var(--paper)" stroke-width="5"/>
      <path d="M0,417 C190,440 390,418 549,437" fill="none" stroke="var(--paper)" stroke-width="4"/>
    </svg>
  </section>

  <section class="slide slide--media">
    <div class="media-panel" role="img" aria-label="Smartphone showing a globe with streams of light and data flowing out of it"></div>
    <p class="brand-name brand-name--corner brand-name--light">KLavender Consulting</p>
  </section>

  <section class="slide slide--closing">
    <p class="brand-name brand-name--hero">KLavender Consulting</p>
    <svg class="wave" viewBox="0 0 549 455" aria-hidden="true">
      <path d="M0,400 C160,420 360,418 549,425 L549,455 L0,455 Z" fill="var(--navy)"/>
      <path d="M0,414 C170,432 370,414 549,433" fill="none" stroke="var(--paper)" stroke-width="4"/>
      <path d="M0,430 C190,446 390,430 549,443" fill="none" stroke="var(--paper)" stroke-width="3"/>
    </svg>
  </section>

</div>
</body>
</html>
```